Short term vacation rental

I need a simple site the we can rent a duplex that is on the sand in Indian rocks beach Fl needs to be able to sync with multiple calendars like staylumo.com qelt tovn using Wordpress

```html
<!DOCTYPE html>
<html lang="en">
<head>
<meta charset="utf-8">
<title>Tideline Retreats – Indian Rocks Beach Duplex</title>
<link href="https://fonts.googleapis.com/css2?family=Marcellus&family=Poppins:wght@300;400;500;600&family=Allison&display=swap" rel="stylesheet">
<style>
:root{
  --navy:#1d3a6b;
  --navy-deep:#183360;
  --teal:#3aa6b9;
  --teal-soft:#cfe9ee;
  --cream:#fdfaf5;
  --white:#ffffff;
  --ink:#23324d;
  --text:#5a6272;
  --line:#e3e6ec;
}
*{margin:0;padding:0;box-sizing:border-box}
html,body{width:1200px;height:4713px;overflow:hidden}
body{position:relative;background:var(--cream);font-family:"Poppins",sans-serif;color:var(--text)}
.abs{position:absolute}
.serif{font-family:"Marcellus",serif;color:var(--ink);font-weight:400;letter-spacing:1px}
.script{font-family:"Allison",cursive;color:var(--teal);font-weight:400}
.btn{position:absolute;display:flex;align-items:center;justify-content:center;font-size:12px;font-weight:500;letter-spacing:.5px;text-transform:uppercase}
.btn-outline{border:1.5px solid var(--navy);color:var(--navy)}
.swoosh{position:absolute;height:3px;border-radius:50%;background:var(--teal)}

/* top bar */
.topbar{left:0;top:0;width:1200px;height:36px;background:var(--navy)}
.social{position:absolute;display:flex;gap:8px}
.social span{width:20px;height:20px;border-radius:50%;border:1.5px solid rgba(255,255,255,.85)}
.topbar .contact{position:absolute;right:142px;top:10px;font-size:12px;color:#fff;display:flex;gap:22px}
.topbar .contact b{font-weight:400;display:flex;align-items:center;gap:6px}

/* header */
.header{left:0;top:36px;width:1200px;height:80px;background:var(--cream)}
.brand{position:absolute;display:flex;flex-direction:column;align-items:center}
.brand .name{font-family:"Marcellus",serif;color:var(--navy);font-size:19px;letter-spacing:1.5px}
.brand .sub{font-family:"Marcellus",serif;color:var(--navy);font-size:9px;letter-spacing:3px}
.nav{position:absolute;left:536px;top:30px;display:flex;gap:30px;font-size:12px;font-weight:500;color:var(--ink)}

/* hero */
.hero{left:0;top:116px;width:1200px;height:564px;background:linear-gradient(100deg,#2b2724 0%,#4a4540 38%,#8e8780 62%,#c9c3ba 100%)}
.hero h1{position:absolute;left:143px;top:219px;font-size:44px;line-height:47px;color:#fff;font-family:"Marcellus",serif;font-weight:400;letter-spacing:1px}

/* about */
.about-bg{left:0;top:1210px;width:1200px;height:332px;background:linear-gradient(180deg,var(--cream) 0%,#e8e6e2 55%,#dcdad6 100%)}
.checks{position:absolute;left:605px;top:1092px;list-style:none}
.checks li{display:flex;align-items:center;gap:8px;font-size:13px;font-weight:500;color:var(--ink);height:36.5px}

/* amenities */
.grid{position:absolute;left:141px;top:1816px;width:920px;display:grid;grid-template-columns:repeat(4,230px);grid-auto-rows:168px}
.cell{display:flex;flex-direction:column;align-items:center;padding-top:18px;text-align:center;border-right:1px solid var(--line)}
.cell:nth-child(4n){border-right:none}
.cell:nth-child(-n+4){border-bottom:1px solid var(--line)}
.cell.active{background:#fff;box-shadow:0 6px 18px rgba(29,58,107,.12);border-bottom:3px solid var(--teal)}
.cell h4{font-size:15px;font-weight:600;color:var(--ink);margin-top:12px}
.cell p{font-size:12px;line-height:19px;color:var(--text);width:175px;margin-top:4px}

/* stats */
.stats{position:absolute;left:635px;top:2941px;display:flex}
.stats div{width:106px;padding-left:8px;border-left:1px solid var(--line)}
.stats div:first-child{border-left:none}
.stats .n{font-family:"Marcellus",serif;font-size:22px;color:var(--ink);line-height:26px}
.stats .l{font-size:10px;letter-spacing:.5px;color:var(--text);text-transform:uppercase}

/* booking */
.card{position:absolute;background:#fff;box-shadow:0 4px 20px rgba(29,58,107,.09)}
.cal{position:absolute;left:30px;top:92px;width:330px;display:grid;grid-template-columns:repeat(7,1fr);font-size:10px;text-align:center;color:var(--ink)}
.cal span{height:30px;display:flex;align-items:center;justify-content:center}
.cal .hd{color:var(--text);height:26px}
.cal .av{background:var(--teal-soft);border-radius:14px;color:var(--navy);margin:4px 2px;height:22px}
.field label{display:block;font-size:12px;font-weight:500;color:var(--ink);margin-bottom:8px}
.field .box{height:46px;border:1px solid var(--line);font-size:11px;color:#9aa1ad;display:flex;align-items:center;justify-content:space-between;padding:0 14px}

/* footer */
.footer{left:0;top:4472px;width:1200px;height:241px;background:var(--navy-deep)}
.fcontact{position:absolute;top:88px;display:flex;align-items:center;gap:14px;color:#fff;font-size:13px;line-height:20px}
.fcontact .ic{width:40px;height:40px;border-radius:50%;background:#fff;display:flex;align-items:center;justify-content:center}
</style>
</head>
<body>

<!-- Top bar -->
<div class="abs topbar">
  <div class="social" style="left:143px;top:8px"><span></span><span></span><span></span><span></span></div>
  <div class="contact">
    <b><svg width="12" height="10" viewBox="0 0 12 10"><rect x="0.5" y="0.5" width="11" height="9" fill="none" stroke="#fff"/><path d="M.5 .5 6 5.5 11.5 .5" fill="none" stroke="#fff"/></svg>Email: info@tidelineretreats.com</b>
    <b><svg width="12" height="12" viewBox="0 0 24 24"><path d="M6.6 10.8a15 15 0 0 0 6.6 6.6l2.2-2.2a1 1 0 0 1 1-.25 11.4 11.4 0 0 0 3.6.57 1 1 0 0 1 1 1V20a1 1 0 0 1-1 1A17 17 0 0 1 3 4a1 1 0 0 1 1-1h3.5a1 1 0 0 1 1 1c0 1.25.2 2.45.57 3.57a1 1 0 0 1-.25 1z" fill="#fff"/></svg>Phone: +1 (727) 555-0184</b>
  </div>
</div>

<!-- Header -->
<header class="abs header">
  <div class="brand" style="left:134px;top:22px">
    <span class="name">TIDELINE RETREATS</span>
    <span class="sub">INDIAN ROCKS BEACH · FLORIDA</span>
  </div>
  <nav class="nav"><span>HOME</span><span>AMENITIES</span><span>GALLERY</span><span>CONTACT US</span></nav>
  <div class="btn btn-outline" style="left:897px;top:15px;width:162px;height:44px;font-size:11px">Check Availability</div>
</header>

<!-- Hero -->
<section class="abs hero" role="img" aria-label="Bright coastal living room with grey sofa, patterned cushions, chandelier and glass coffee table"></section>
<div class="abs script" style="left:140px;top:225px;font-size:86px;color:#fff;line-height:1">Indian Rocks Beach</div>
<h1 class="abs" style="left:143px;top:336px;font-size:45px;line-height:47px;color:#fff;font-family:'Marcellus',serif;font-weight:400;letter-spacing:1px">YOUR PRIVATE<br>PARADISE ON SAND</h1>
<p class="abs" style="left:143px;top:436px;width:490px;font-size:13px;line-height:25px;color:#fff">Wake up to sunrise over the Gulf, fall asleep to waves. This beautifully updated duplex is the ultimate Indian Rocks Beach escape.</p>
<div class="btn" style="left:143px;top:506px;width:186px;height:43px;background:#fff;color:var(--navy);font-size:11px">View Rates &amp; Availability</div>
<div class="btn" style="left:372px;top:506px;width:164px;height:43px;border:1.5px solid #fff;color:#fff;font-size:11px">Call (727) 555-0147</div>

<!-- About -->
<div class="abs about-bg" role="img" aria-label="Faded aerial view of the beachfront skyline and shoreline"></div>
<div class="abs" style="left:179px;top:757px;width:346px;height:440px;border:2px solid var(--teal)"></div>
<div class="abs" role="img" aria-label="Woman on a balcony overlooking white stucco villas with tiled roofs" style="left:0;top:777px;width:507px;height:522px;background:linear-gradient(160deg,#c9d7e3 0%,#e7ddd1 35%,#a37a5c 70%,#5e6b58 100%)"></div>
<div class="abs" style="left:305px;top:1139px;width:258px;height:218px;background:#fff;box-shadow:0 4px 18px rgba(0,0,0,.12)"></div>
<div class="abs" role="img" aria-label="Beachfront duplex with balconies above the sand" style="left:315px;top:1149px;width:238px;height:198px;background:linear-gradient(180deg,#5d8fd0 0%,#8fb6df 40%,#4a5560 62%,#d9cdb3 100%)"></div>

<div class="abs script" style="left:603px;top:750px;font-size:66px;line-height:1">About</div>
<h2 class="abs serif" style="left:603px;top:810px;font-size:45px;line-height:47px">WHERE THE GULF<br>MEETS COMFORT</h2>
<div class="swoosh" style="left:607px;top:908px;width:230px"></div>
<h3 class="abs" style="left:605px;top:938px;font-size:14px;font-weight:600;color:var(--ink)">STEPS FROM THE SUGAR-SAND BEACH</h3>
<p class="abs" style="left:605px;top:965px;width:450px;font-size:12.5px;line-height:24px">Shoreline Duplex is a rare beachfront gem — literally on the sand. Located on the serene shores of Indian Rocks Beach, our property offers two beautifully appointed units or can be rented as a full home for larger groups. Breathtaking sunsets, dolphin sightings, and endless coastal serenity.</p>
<ul class="checks">
  <li><svg width="14" height="14" viewBox="0 0 14 14"><circle cx="7" cy="7" r="7" fill="var(--navy)"/><path d="M4 7.2 6.1 9.2 10 5" fill="none" stroke="#fff" stroke-width="1.6"/></svg>Direct private beach access — no roads to cross</li>
  <li><svg width="14" height="14" viewBox="0 0 14 14"><circle cx="7" cy="7" r="7" fill="var(--navy)"/><path d="M4 7.2 6.1 9.2 10 5" fill="none" stroke="#fff" stroke-width="1.6"/></svg>3 spacious bedrooms / sleeps 8 comfortably</li>
  <li><svg width="14" height="14" viewBox="0 0 14 14"><circle cx="7" cy="7" r="7" fill="var(--navy)"/><path d="M4 7.2 6.1 9.2 10 5" fill="none" stroke="#fff" stroke-width="1.6"/></svg>Fully renovated kitchen &amp; spa-inspired baths</li>
  <li><svg width="14" height="14" viewBox="0 0 14 14"><circle cx="7" cy="7" r="7" fill="var(--navy)"/><path d="M4 7.2 6.1 9.2 10 5" fill="none" stroke="#fff" stroke-width="1.6"/></svg>Expansive oceanfront deck with lounge chairs</li>
  <li><svg width="14" height="14" viewBox="0 0 14 14"><circle cx="7" cy="7" r="7" fill="var(--navy)"/><path d="M4 7.2 6.1 9.2 10 5" fill="none" stroke="#fff" stroke-width="1.6"/></svg>Beach gear: chairs, umbrella, cooler &amp; towels</li>
</ul>
<div class="btn btn-outline" style="left:605px;top:1280px;width:162px;height:44px;font-size:11px;border-color:#7b8699">Check Availability</div>

<!-- Amenities -->
<div class="abs script" style="left:0;width:1200px;text-align:center;top:1616px;font-size:62px;line-height:1">Amenities</div>
<h2 class="abs serif" style="left:0;width:1200px;text-align:center;top:1674px;font-size:44px;line-height:46px">BEACHFRONT<br>LUXURY &amp; COMFORT</h2>
<div class="swoosh" style="left:518px;top:1771px;width:164px"></div>

<div class="grid">
  <div class="cell"><svg width="64" height="60" viewBox="0 0 64 60" fill="none" stroke="var(--navy)" stroke-width="2"><circle cx="22" cy="14" r="6" stroke="var(--teal)"/><path d="M8 50h48M14 50l6-18h24l6 18M20 32l4-14 18 6" /><path d="M6 56h52" stroke="var(--teal)"/></svg><h4>Beachfront Deck</h4><p>Unobstructed Gulf Views, Outdoor Dining &amp; BBQ Grill</p></div>
  <div class="cell active"><svg width="64" height="60" viewBox="0 0 64 60" fill="none" stroke="var(--navy)" stroke-width="2"><rect x="10" y="4" width="44" height="12"/><rect x="12" y="26" width="40" height="30"/><path d="M12 38h40M32 26v30" /><circle cx="22" cy="32" r="2" stroke="var(--teal)"/><circle cx="42" cy="32" r="2" stroke="var(--teal)"/></svg><h4>Chef's Kitchen</h4><p>Quartz Counters, Full Appliances, Drip &amp; Pod Brewer</p></div>
  <div class="cell"><svg width="64" height="60" viewBox="0 0 64 60" fill="none" stroke="var(--navy)" stroke-width="2"><rect x="20" y="4" width="24" height="16" stroke="var(--teal)"/><path d="M8 56V30h48v26M8 42h48M14 30v-6h16v6M34 30v-6h16v6"/></svg><h4>Serene Bedrooms</h4><p>King Master + Queen + Twin Bunks, Premium Linens</p></div>
  <div class="cell"><svg width="64" height="60" viewBox="0 0 64 60" fill="none" stroke="var(--navy)" stroke-width="2"><rect x="8" y="8" width="40" height="34"/><path d="M4 50h48" /><path d="M40 30a12 12 0 0 1 18 0M44 36a6 6 0 0 1 10 0" stroke="var(--teal)"/></svg><h4>High-Speed WiFi</h4><p>500 Mbps, Remote Work &amp; Streaming Ready</p></div>
  <div class="cell"><svg width="64" height="60" viewBox="0 0 64 60" fill="none" stroke="var(--navy)" stroke-width="2"><path d="M6 24 32 6l26 18v32H6z"/><rect x="16" y="32" width="32" height="14" stroke="var(--teal)"/><circle cx="22" cy="50" r="3"/><circle cx="42" cy="50" r="3"/></svg><h4>Private Parking</h4><p>Off-Street Parking For 4 Vehicles + EV Charger</p></div>
  <div class="cell"><svg width="64" height="60" viewBox="0 0 64 60" fill="none" stroke="var(--navy)" stroke-width="2"><path d="M10 22a22 22 0 0 1 44 0z" /><path d="M32 22v30" /><path d="M8 56h48" stroke="var(--teal)"/><circle cx="20" cy="46" r="5" stroke="var(--teal)"/></svg><h4>Beach Concierge</h4><p>Chairs, Toys, Boogie Boards – We've Got You</p></div>
  <div class="cell"><svg width="64" height="60" viewBox="0 0 64 60" fill="none" stroke="var(--navy)" stroke-width="2"><ellipse cx="32" cy="42" rx="12" ry="10"/><circle cx="16" cy="24" r="5"/><circle cx="26" cy="14" r="5"/><circle cx="38" cy="14" r="5"/><circle cx="48" cy="24" r="5"/></svg><h4>Pet-Friendly</h4><p>Lorem Ipsum Is Dummy Rinting And Typesetting</p></div>
  <div class="cell"><svg width="64" height="60" viewBox="0 0 64 60" fill="none" stroke="var(--navy)" stroke-width="2"><path d="M14 56V8h14v8"/><path d="M22 22v4M28 24v4M34 22v4M25 32v4M31 32v4" stroke="var(--teal)"/><path d="M44 56V34M44 34a8 14 0 1 1 0-1"/></svg><h4>Outdoor Shower &amp; Patio</h4><p>Lorem Ipsum Is Dummy Rinting And Typesetting</p></div>
</div>
<div class="btn btn-outline" style="left:519px;top:2189px;width:162px;height:44px;font-size:11px;border-color:#7b8699">Check Availability</div>

<!-- Coast band -->
<div class="abs" role="img" aria-label="Sandy beach lined with palm trees under a blue sky with turquoise water" style="left:0;top:2323px;width:1200px;height:445px;background:linear-gradient(180deg,#2f74c4 0%,#7fb0e2 40%,#3e8a63 62%,#e8d7b5 85%,#f1e6cf 100%)"></div>
<div class="abs" style="left:113px;top:2383px;width:463px;height:291px;background:#fff"></div>
<h2 class="abs serif" style="left:139px;top:2420px;font-size:38px;line-height:40px">A QUIETER SIDE OF<br>THE GULF COAST.</h2>
<p class="abs" style="left:139px;top:2512px;width:410px;font-size:13px;line-height:25px">Tucked along a beloved stretch of Florida coastline, Indian Rocks Beach is known for soft sand, slower days, and a welcoming neighborhood feel.</p>
<div class="btn btn-outline" style="left:139px;top:2594px;width:142px;height:44px;font-size:11px">Plan Your Stay</div>

<!-- Gallery -->
<div class="abs script" style="left:138px;top:2830px;font-size:66px;line-height:1">Gallery</div>
<h2 class="abs serif" style="left:139px;top:2912px;font-size:43px;line-height:46px">SUNRISE TO<br>SUNSET DUPLEX</h2>
<div class="swoosh" style="left:141px;top:3006px;width:160px"></div>
<p class="abs" style="left:635px;top:2875px;width:420px;font-size:12px;line-height:18px">Set along the shoreline of Indian Rocks Beach, this duplex offers an easygoing coastal base with bright interiors, everyday comforts, and the Gulf just steps away.</p>
<div class="stats">
  <div><div class="n">03</div><div class="l">Bedrooms</div></div>
  <div><div class="n">02</div><div class="l">Baths</div></div>
  <div><div class="n">06</div><div class="l">Guests</div></div>
  <div><div class="n">0</div><div class="l">Steps to Stand</div></div>
</div>
<div class="abs" role="img" aria-label="Bright bedroom with large bed, beige linens and tall window" style="left:141px;top:3049px;width:530px;height:505px;background:linear-gradient(160deg,#f1ede7 0%,#dcd3c7 45%,#b79a7c 75%,#8a7968 100%)"></div>
<div class="abs" role="img" aria-label="Modern white kitchen with marble island and wood cabinets" style="left:682px;top:3049px;width:375px;height:245px;background:linear-gradient(135deg,#f4f3f1 0%,#dad8d5 55%,#8f5a3e 100%)"></div>
<div class="abs" role="img" aria-label="Bathroom with dark vanity and glass shower" style="left:682px;top:3313px;width:183px;height:241px;background:linear-gradient(160deg,#d8d4cf 0%,#8a7663 55%,#4a3b30 100%)"></div>
<div class="abs" role="img" aria-label="Deck with lounge chairs and striped umbrella over the sea" style="left:876px;top:3313px;width:181px;height:241px;background:linear-gradient(180deg,#4aa3d8 0%,#8fd0ea 45%,#2d8fb2 62%,#6b3a2a 100%)"></div>

<!-- Availability -->
<div class="abs script" style="left:0;width:1200px;text-align:center;top:3632px;font-size:62px;line-height:1">Amenities</div>
<h2 class="abs serif" style="left:0;width:1200px;text-align:center;top:3690px;font-size:42px;line-height:44px">CHECK AVAILABILITY<br>&amp; RESERVE YOUR STAY</h2>
<div class="swoosh" style="left:540px;top:3785px;width:120px"></div>
<p class="abs" style="left:0;width:1200px;text-align:center;top:3812px;font-size:12.5px;color:var(--ink)">Select your dates and send an inquiry — immediate response from our local team.</p>

<div class="card" style="left:141px;top:3868px;width:393px;height:503px">
  <div class="abs serif" style="left:28px;top:26px;font-size:24px">CHECK AVAILABILITY</div>
  <div class="abs" style="left:30px;top:66px;display:flex;align-items:center;gap:10px;font-size:14px;font-weight:600;color:var(--ink)">
    <svg width="14" height="14" viewBox="0 0 14 14"><rect x="1" y="2" width="12" height="11" fill="none" stroke="var(--navy)" stroke-width="1.5"/><path d="M1 5h12" stroke="var(--navy)" stroke-width="1.5"/></svg>May 2026</div>
  <div class="abs" style="left:350px;top:64px;display:flex;gap:8px">
    <svg width="20" height="20" viewBox="0 0 20 20"><circle cx="10" cy="10" r="10" fill="#eef1f5"/><path d="M11.5 6 7.5 10l4 4" fill="none" stroke="var(--ink)" stroke-width="1.5"/></svg>
    <svg width="20" height="20" viewBox="0 0 20 20"><circle cx="10" cy="10" r="10" fill="#eef1f5"/><path d="M8.5 6l4 4-4 4" fill="none" stroke="var(--ink)" stroke-width="1.5"/></svg>
  </div>
  <div class="cal">
    <span class="hd">Su</span><span class="hd">Mo</span><span class="hd">Tu</span><span class="hd">We</span><span class="hd">Th</span><span class="hd">Fr</span><span class="hd">Sa</span>
    <span></span><span></span><span></span><span></span><span></span><span>1</span><span>2</span>
    <span>3</span><span>4</span><span>5</span><span>6</span><span>7</span><span>8</span><span>9</span>
    <span class="av">10</span><span class="av">11</span><span class="av">12</span><span>13</span><span>14</span><span>15</span><span>16</span>
    <span>17</span><span>18</span><span>19</span><span class="av">20</span><span class="av">21</span><span class="av">22</span><span>23</span>
    <span>24</span><span>25</span><span>26</span><span>27</span><span>28</span><span>29</span><span>30</span>
    <span>31</span>
  </div>
  <div class="abs" style="left:30px;top:338px;width:330px;border-top:1px solid var(--line)"></div>
  <div class="abs" style="left:30px;top:350px;width:330px;display:flex;justify-content:space-between;font-size:9px;color:#9aa1ad">
    <span><i style="display:inline-block;width:7px;height:7px;border-radius:50%;background:#9fd9b6;margin-right:5px"></i>Available</span>
    <span><i style="display:inline-block;width:7px;height:7px;border-radius:50%;background:#f3b7b7;margin-right:5px"></i>Booked</span>
    <span><i style="display:inline-block;width:7px;height:7px;border-radius:50%;background:var(--teal);margin-right:5px"></i>Selected</span>
  </div>
  <div class="abs" style="left:30px;top:382px;width:378px;max-width:333px;height:52px;background:#eef4fb;border-radius:4px;padding:10px 12px;font-size:10px;color:var(--text)">
    Your dates:<br><b style="color:var(--ink);font-size:11px;font-weight:600">None selected</b>
    <span style="position:absolute;right:14px;top:20px;font-size:9px;color:var(--teal)">Clear</span>
  </div>
</div>

<div class="card" style="left:609px;top:3868px;width:448px;height:503px">
  <div class="abs serif" style="left:18px;top:30px;font-size:24px">REQUEST TO BOOK</div>
  <div class="abs" style="left:18px;top:64px;font-size:11.5px">Fill out the form and we'll confirm rates &amp; availability.</div>
  <div class="abs field" style="left:18px;top:104px;width:204px"><label>Full name</label><div class="box">John Carter</div></div>
  <div class="abs field" style="left:229px;top:104px;width:204px"><label>Email address</label><div class="box">hello@example.com</div></div>
  <div class="abs field" style="left:18px;top:185px;width:204px"><label>Check-in</label><div class="box">dd-mm-yyyy<svg width="14" height="14" viewBox="0 0 14 14"><rect x="1" y="2" width="12" height="11" fill="none" stroke="#9aa1ad"/><path d="M1 5h12" stroke="#9aa1ad"/></svg></div></div>
  <div class="abs field" style="left:229px;top:185px;width:204px"><label>Check-out</label><div class="box">dd-mm-yyyy<svg width="14" height="14" viewBox="0 0 14 14"><rect x="1" y="2" width="12" height="11" fill="none" stroke="#9aa1ad"/><path d="M1 5h12" stroke="#9aa1ad"/></svg></div></div>
  <div class="abs field" style="left:18px;top:266px;width:415px"><label>Guests</label><div class="box">1 Guest<svg width="12" height="8" viewBox="0 0 12 8"><path d="M1 1l5 5 5-5" fill="none" stroke="var(--ink)" stroke-width="1.5"/></svg></div></div>
  <div class="abs field" style="left:18px;top:347px;width:415px"><label>Special requests (optional)</label><div class="box">Any questions?<svg width="12" height="8" viewBox="0 0 12 8"><path d="M1 1l5 5 5-5" fill="none" stroke="var(--ink)" stroke-width="1.5"/></svg></div></div>
  <div class="btn" style="left:18px;top:431px;width:415px;height:46px;background:var(--navy);color:#fff;font-size:11.5px">Check Rates &amp; Book Now</div>
</div>

<!-- Footer -->
<footer class="abs footer">
  <div class="fcontact" style="left:234px">
    <div class="ic"><svg width="18" height="18" viewBox="0 0 24 24"><path d="M6.6 10.8a15 15 0 0 0 6.6 6.6l2.2-2.2a1 1 0 0 1 1-.25 11.4 11.4 0 0 0 3.6.57 1 1 0 0 1 1 1V20a1 1 0 0 1-1 1A17 17 0 0 1 3 4a1 1 0 0 1 1-1h3.5a1 1 0 0 1 1 1c0 1.25.2 2.45.57 3.57a1 1 0 0 1-.25 1z" fill="var(--navy)"/></svg></div>
    <div>Call Us<br>(727) 555-0184</div>
  </div>
  <div class="brand" style="left:478px;top:92px;width:244px">
    <span class="name" style="color:#fff;font-size:22px">TIDELINE RETREATS</span>
    <span class="sub" style="color:#fff">INDIAN ROCKS BEACH · FLORIDA</span>
  </div>
  <div class="fcontact" style="left:766px">
    <div class="ic"><svg width="16" height="13" viewBox="0 0 12 10"><rect x="0.5" y="0.5" width="11" height="9" fill="none" stroke="var(--navy)"/><path d="M.5 .5 6 5.5 11.5 .5" fill="none" stroke="var(--navy)"/></svg></div>
    <div>Email<br>info@tidelineretreats.com</div>
  </div>
  <div class="abs" style="left:143px;top:208px;font-size:11.5px;color:#fff">© 2026 Tideline Retreats. All Rights Reserved.</div>
  <div class="social" style="left:923px;top:204px"><span style="width:26px;height:26px;background:var(--teal);border-color:var(--teal)"></span><span style="width:26px;height:26px"></span><span style="width:26px;height:26px"></span><span style="width:26px;height:26px"></span></div>
</footer>

</body>
</html>
```